professional business card design

Business card design. Photos have been uploaded and i am open to the designer choosing which photos to use. Would like the card to be mostyly in a grey scale design with black, whites, silver & grey colours. I have added copy of our flyer as would like on the back side of card our services to be listed. Do not use any bright colurs such as blue red green or yellow. i need to be able to edit the phone number and naem in the final card design submitted.

Target Market(s)

Clients

Industry/Entity Type

earhmovibng and transport

Contact Information for Business Card

Director Name, address, email, phone number and services

Colors

Designer to choose only greyscale colors for use in the design.

Requirements
Should not have
• no yellow, red, blue or green

```html
<!DOCTYPE html>
<html lang="en">
<head>
<meta charset="utf-8">
<title>Ridgeline Pty Ltd – Business Card</title>
<link href="https://fonts.googleapis.com/css2?family=Roboto:wght@300;400;700&display=swap" rel="stylesheet">
<style>
  :root {
    --page: #ececec;
    --black: #050505;
    --charcoal: #1b1b1b;
    --steel: #6a6a6a;
    --silver: #bdbdbd;
    --white: #ffffff;
    --ink: #111111;
    --ink-soft: #2a2a2a;
    --list: #e4e4e4;
  }
  * { box-sizing: border-box; margin: 0; padding: 0; }
  html, body { width: 1106px; height: 1200px; overflow: hidden; }
  body {
    background: var(--page);
    font-family: "Roboto", Arial, sans-serif;
    position: relative;
  }
  .card {
    position: absolute;
    left: 131px;
    width: 842px;
    height: 492px;
    overflow: hidden;
    box-shadow: 0 4px 8px rgba(0,0,0,0.25);
  }
  /* Front */
  .card-front {
    top: 85px;
    background: linear-gradient(to bottom, var(--black) 0%, var(--charcoal) 30%, var(--steel) 52%, var(--silver) 70%, var(--white) 92%);
  }
  .fleet-photo {
    position: absolute;
    left: 14px; top: 140px;
    width: 815px; height: 172px;
    background: linear-gradient(to bottom, #2a2a2a 0%, #3b3b3b 55%, #8e8e8e 100%);
    opacity: 0.85;
  }
  .brand {
    position: absolute;
    left: 0; right: 0; top: 38px;
    text-align: center;
    color: var(--white);
  }
  .brand-name {
    font-weight: 700;
    font-size: 64px;
    letter-spacing: 2px;
    line-height: 1;
  }
  .brand-suffix {
    font-weight: 700;
    font-size: 20px;
    margin-top: 6px;
    color: var(--silver);
  }
  .slash {
    position: absolute;
    left: 0; top: 0;
  }
  .person {
    position: absolute;
    left: 97px; top: 360px;
    color: var(--ink);
  }
  .person-name {
    font-weight: 400;
    font-size: 35px;
    letter-spacing: 0.5px;
  }
  .person-role {
    font-weight: 300;
    font-size: 21px;
    margin-top: 6px;
    color: var(--ink-soft);
  }
  .contact-list {
    position: absolute;
    right: 48px; top: 331px;
    list-style: none;
    text-align: right;
    color: var(--ink);
    font-weight: 400;
    font-size: 20px;
  }
  .contact-list li {
    height: 32.5px;
    display: flex;
    align-items: center;
    justify-content: flex-end;
    gap: 14px;
  }
  .contact-list svg { width: 13px; height: 13px; fill: var(--ink); }
  /* Back */
  .card-back {
    top: 622px;
    background: var(--black);
  }
  .services-title {
    position: absolute;
    left: 58px; top: 46px;
    color: var(--white);
    font-weight: 700;
    font-size: 40px;
    z-index: 2;
  }
  .services-list {
    position: absolute;
    left: 56px; top: 116px;
    list-style: none;
    color: var(--list);
    font-weight: 300;
    font-size: 21px;
    line-height: 27.2px;
    z-index: 2;
  }
  .services-list li::before { content: "• "; }
  .services-list .wrap { padding-left: 11px; }
  .services-list .wrap::before { content: ""; }
  .truck-photo {
    position: absolute;
    left: 400px; top: 167px;
    width: 425px; height: 305px;
    background: linear-gradient(120deg, #1a1a1a 0%, #3a3a3a 45%, #6d6d6d 80%, #9a9a9a 100%);
    border-radius: 30px 30px 8px 8px;
    z-index: 1;
  }
</style>
</head>
<body>
  <section class="card card-front">
    <div class="fleet-photo" role="img" aria-label="Photo of a black road train with three tipper trailers on a dirt yard"></div>
    <div class="brand">
      <div class="brand-name">RIDGELINE</div>
      <div class="brand-suffix">Pty Ltd</div>
    </div>
    <svg class="slash" width="842" height="492" viewBox="0 0 842 492" aria-hidden="true">
      <path d="M457 280 L373 459 L376 457 Z" fill="var(--black)"/>
    </svg>
    <div class="person">
      <div class="person-name">DALE MARSH</div>
      <div class="person-role">General Manager</div>
    </div>
    <ul class="contact-list">
      <li>401-555-0147
        <svg viewBox="0 0 24 24"><path d="M6.6 10.8a15.1 15.1 0 0 0 6.6 6.6l2.2-2.2a1 1 0 0 1 1-.25 11.4 11.4 0 0 0 3.6.6 1 1 0 0 1 1 1V20a1 1 0 0 1-1 1A17 17 0 0 1 3 4a1 1 0 0 1 1-1h3.5a1 1 0 0 1 1 1c0 1.250.2 2.450.6 3.6a1 1 0 0 1-.25 1z"/></svg>
      </li>
      <li>dmarsh@ridgeline.com
        <svg viewBox="0 0 24 24"><path d="M2 5h20v14H2z" fill="var(--ink)"/><path d="M3 6l9 7 9-7" stroke="var(--white)" stroke-width="1.6" fill="none"/></svg>
      </li>
      <li>www.ridgeline.com
        <svg viewBox="0 0 24 24"><circle cx="12" cy="12" r="10"/><path d="M2 12h20M12 2c3 3 3 17 0 20M12 2c-3 3-3 17 0 20" stroke="var(--white)" stroke-width="1.4" fill="none"/></svg>
      </li>
      <li>14 Quarry Rd, Ashby RI 02000
        <svg viewBox="0 0 24 24"><circle cx="12" cy="8" r="4"/><path d="M4 21c0-4 4-7 8-7s8 3 8 7z"/></svg>
      </li>
    </ul>
  </section>

  <section class="card card-back">
    <h2 class="services-title">Our Services</h2>
    <ul class="services-list">
      <li>Over size loades/Hot shots loads</li>
      <li>Heavy vehicle recovery services</li>
      <li>Portable Water Deliveries</li>
      <li>Road Buildings/Maintenance</li>
      <li>Earthworks</li>
      <li>Sand &amp; Metal Supply &amp; Cartage</li>
      <li>Road Train Tippers</li>
      <li>Road Train Tankers</li>
      <li>Road Train Flat Tops</li>
      <li>Drop Deck Trailers</li>
      <li>Mine Site accredited</li>
      <li class="wrap">equipment &amp; Operators</li>
    </ul>
    <div class="truck-photo" role="img" aria-label="Photo of a black prime mover with bull bar hauling a silver tanker trailer"></div>
  </section>
</body>
</html>
```